Bright Horizon Painting and Remodeling needs a business card

Business card should have company logo. I will upload two different logos and let me see which one is a better design for the business card.

Name of company: Bright Horizon Painting and Remodeling
Address: 4126 NW 71st st Suite 214
Bayview, FL 33199

local phone: (305) 555-0142
toll free (855) 555-0197
fax (866) 555-0163

email: corinne@paintingbrighthorizon.example

not sure if i should include social media links or names on the business card.

company does interior and exterior painting, pressure washing, wall paper removal, drywall and stucco repair, staining,

We give free estimates.

I want a two sided business card.

Not sure if all this information is necessary for the business card. Designer can pick out whatever information they deem is important for a consumer to see on the business card.

Anticipating on the business card to be printed on nice quality.

I will upload an image of one of the logos on a type of business card surface. That idea can be used as well. Be creative. Business card should be professional but very nice and eye catching.

remove drywall and stucco repair and replace with tile installation

Industry/Entity Type

Business

Contact Information for Business Card

Bayview, FL 33199

toll free (855) 555-0197
fax (866) 555-0163

company does interior and exterior painting, pressure washing, wall paper removal, drywall and stucco repair, staining, tile removal, *specializing in vinyl floor removal

free estimates.

Requirements
Must have
• Profesional font

```html
<!DOCTYPE html>
<html lang="en">
<head>
<meta charset="utf-8">
<title>Bright Horizon Painting and Remodeling – Business Card</title>
<link href="https://fonts.googleapis.com/css2?family=Merriweather:wght@700;900&family=Questrial&display=swap" rel="stylesheet">
<style>
  :root {
    --card-dark: #1f1f1f;
    --card-light: #ffffff;
    --brand-blue: #1387c4;
    --fold-blue: #1b5878;
    --ink: #333333;
    --page: #ffffff;
    --edge: #000000;
  }
  html, body {
    margin: 0;
    padding: 0;
    width: 1200px;
    height: 1000px;
    overflow: hidden;
    background: var(--page);
  }
  .sheet { position: relative; width: 1200px; height: 1000px; }

  .card {
    position: absolute;
    left: 154px;
    width: 901px;
    height: 389px;
    border: 1.5px solid var(--edge);
    border-radius: 2px;
    overflow: hidden;
    background: var(--card-dark);
  }
  .card--front { top: 89px; }
  .card--back { top: 522px; }

  .card__art { position: absolute; inset: 0; }

  .brand {
    position: absolute;
    display: flex;
    align-items: center;
    gap: 12px;
    color: var(--card-light);
    font-family: "Merriweather", Georgia, serif;
    font-weight: 900;
    text-transform: uppercase;
    line-height: 1.2;
  }
  .brand__dot {
    flex: none;
    border-radius: 50%;
    background: var(--brand-blue);
  }
  .card--front .brand { left: 66px; top: 150px; width: 220px; font-size: 17px; }
  .card--front .brand__dot { width: 34px; height: 34px; }
  .card--back .brand { left: 300px; top: 134px; width: 310px; font-size: 23px; }
  .card--back .brand__dot { width: 44px; height: 44px; }

  .title-band {
    position: absolute;
    left: 318px;
    top: 106px;
    width: 583px;
    height: 40px;
    display: flex;
    align-items: center;
    justify-content: center;
    color: var(--card-light);
    font-family: "Merriweather", Georgia, serif;
    font-weight: 900;
    font-size: 18.5px;
    letter-spacing: 0.3px;
    text-transform: uppercase;
  }

  .contact__row {
    position: absolute;
    left: 419px;
    display: flex;
    align-items: flex-start;
    gap: 6px;
    font-family: "Questrial", Arial, sans-serif;
    font-weight: 400;
    color: var(--ink);
    font-size: 19px;
    letter-spacing: 0.9px;
    -webkit-text-stroke: 0.8px var(--ink);
    white-space: nowrap;
  }
  .contact__row--phone { top: 201px; }
  .contact__row--address { top: 258px; }
  .contact__icon { flex: none; width: 41px; height: 41px; }
  .contact__lines { text-align: center; line-height: 22px; padding-top: 14px; }
  .contact__row--address .contact__lines { padding-top: 9px; }
</style>
</head>
<body>
<main class="sheet">

  <section class="card card--front" aria-label="Business card front">
    <svg class="card__art" width="901" height="389" viewBox="0 0 901 389" aria-hidden="true">
      <path d="M626 0 H901 V389 H183 C330 290 480 150 626 0 Z" fill="var(--card-light)"/>
      <path d="M318 146 L392 146 L424 180 L391 211 Z" fill="var(--fold-blue)"/>
      <rect x="318" y="106" width="583" height="40" fill="var(--brand-blue)"/>
    </svg>

    <div class="brand">
      <span class="brand__dot"></span>
      <span class="brand__name">Bright Horizon Painting and Remodeling</span>
    </div>

    <div class="title-band">Bright Horizon Painting and Remodeling</div>

    <div class="contact__row contact__row--phone">
      <svg class="contact__icon" viewBox="0 0 41 41" aria-label="Phone">
        <circle cx="20.5" cy="20.5" r="20.5" fill="var(--brand-blue)"/>
        <path d="M9 17 C12 10 29 10 32 17 L28 19 L26 16 C23 15 18 15 15 16 L13 19 Z" fill="#fff"/>
        <path d="M13 21 H28 L30 30 H11 Z" fill="#fff"/>
        <circle cx="20.5" cy="25" r="2.6" fill="var(--brand-blue)"/>
      </svg>
      <div class="contact__lines">
        (305) 555-0142 toll free (855) 555-0197<br>
        fax (866) 555-0163
      </div>
    </div>
    <div class="contact__row contact__row--address">
      <svg class="contact__icon" viewBox="0 0 41 41" aria-label="Address">
        <circle cx="20.5" cy="20.5" r="20.5" fill="var(--brand-blue)"/>
        <path d="M8 20 L20.5 9 L33 20 Z" fill="#fff"/>
        <rect x="11" y="19" width="19" height="12" fill="#fff"/>
        <rect x="14" y="22" width="4" height="4" fill="var(--brand-blue)"/>
        <rect x="23" y="22" width="4" height="4" fill="var(--brand-blue)"/>
        <rect x="19" y="25" width="3" height="6" fill="var(--brand-blue)"/>
      </svg>
      <div class="contact__lines">4126 NW 71st st Suite 214 Bayview, FL 33199</div>
    </div>
  </section>

  <section class="card card--back" aria-label="Business card back">
    <svg class="card__art" width="901" height="389" viewBox="0 0 901 389" aria-hidden="true">
      <rect x="0" y="332" width="901" height="6" fill="var(--card-light)"/>
      <rect x="0" y="338" width="901" height="51" fill="var(--brand-blue)"/>
    </svg>

    <div class="brand">
      <span class="brand__dot"></span>
      <span class="brand__name">Bright Horizon Painting and Remodeling</span>
    </div>
  </section>

</main>
</body>
</html>
```